New Business Card

We need to refresh our business cards. We designed these ourselves and we have no graphic design experience. We would like to find a new business card design that is professional and unique. We are an auto finance company. Feel free to play with the logo, but we would like to keep the eye very present on the card. Our corporate colors are green, grey, and white.
Green - RGB - 168,215,27; HEX - #AADD22
Grey - RGB - 196,196,196; HEX - #C4C4C4
Updates
Need to upload the vector file to finalize the project. The last logo was for a jpeg that didn't stretch well.
Industry/Entity Type
Financial Service
Contact Information for Business Card
Honestly don't know...I need your help!

```html
<!DOCTYPE html>
<html lang="en">
<head>
<meta charset="utf-8">
<title>Farview Capital – Business Card</title>
<link rel="stylesheet" href="https://fonts.googleapis.com/css2?family=Ubuntu:wght@400;500;700&display=swap">
<style>
  :root {
    --bg: #2b2623;
    --card: #141516;
    --card-front: #18191a;
    --green: #aadd22;
    --grey: #c4c4c4;
    --white: #ffffff;
    --divider: #4a4b4d;
  }
  * { margin: 0; padding: 0; box-sizing: border-box; }
  html, body { width: 1200px; height: 769px; overflow: hidden; }
  body {
    background: var(--bg);
    font-family: "Ubuntu", sans-serif;
    position: relative;
  }
  .card {
    position: absolute;
    top: 230px;
    width: 540px;
    height: 309px;
    border-radius: 3px;
    box-shadow: 0 10px 30px rgba(0,0,0,.45);
  }
  .card-front { left: 40px; background: var(--card-front); }
  .card-back { left: 620px; background: var(--card); }

  .front-brand {
    position: absolute;
    left: 0; right: 0; top: 0; bottom: 0;
    display: flex;
    align-items: center;
    justify-content: center;
    gap: 16px;
  }
  .brand-dot {
    width: 54px; height: 54px;
    border-radius: 50%;
    background: var(--grey);
  }
  .brand-name {
    font-size: 34px;
    font-weight: 500;
    color: var(--grey);
    letter-spacing: .5px;
  }

  .back-brand {
    position: absolute;
    left: 30px; top: 0; bottom: 0;
    width: 215px;
    display: flex;
    flex-direction: column;
    align-items: center;
    justify-content: center;
    gap: 14px;
  }
  .back-brand .brand-dot { width: 90px; height: 90px; background: var(--green); }
  .back-brand .brand-name { font-size: 22px; color: var(--grey); }

  .divider {
    position: absolute;
    left: 262px; top: 48px;
    width: 1px; height: 213px;
    background: var(--divider);
  }
  .contact {
    position: absolute;
    left: 284px; top: 60px;
    color: var(--white);
  }
  .person-name {
    font-size: 22px;
    font-weight: 700;
    color: var(--green);
    line-height: 1;
  }
  .person-title {
    font-size: 12px;
    color: var(--grey);
    letter-spacing: .5px;
    margin-top: 4px;
  }
  .address {
    font-size: 12px;
    line-height: 16px;
    margin-top: 12px;
  }
  .details { list-style: none; margin-top: 12px; }
  .details li {
    font-size: 12px;
    line-height: 17px;
    display: flex;
    align-items: center;
    gap: 7px;
  }
  .details svg { width: 10px; height: 10px; fill: var(--green); flex: none; }
</style>
</head>
<body>
  <section class="card card-front">
    <div class="front-brand">
      <span class="brand-dot"></span>
      <span class="brand-name">Farview Capital</span>
    </div>
  </section>

  <section class="card card-back">
    <div class="back-brand">
      <span class="brand-dot"></span>
      <span class="brand-name">Farview Capital</span>
    </div>
    <div class="divider"></div>
    <div class="contact">
      <p class="person-name">DANIEL REYES</p>
      <p class="person-title">CEO/FOUNDER</p>
      <p class="address">4120 Juniper Court<br>Anchorage, Alaska 34561</p>
      <ul class="details">
        <li><svg viewBox="0 0 10 10"><path d="M2 0h2l1 3-1.5 1a6 6 0 0 0 2.5 2.5L7 5l3 1v2a2 2 0 0 1-2 2C4 10 0 6 0 2a2 2 0 0 1 2-2z"/></svg>555 214 7302</li>
        <li><svg viewBox="0 0 10 10"><path d="M2.5 0h5a1 1 0 0 1 1 1v8a1 1 0 0 1-1 1h-5a1 1 0 0 1-1-1V1a1 1 0 0 1 1-1zm.5 1.5v6h4v-6z"/></svg>555 390 6118</li>
        <li><svg viewBox="0 0 10 10"><path d="M2 0h5v3H2zM0 3.5h10V9H0zm2 2v1h6v-1z"/></svg>555 782 4456</li>
        <li><svg viewBox="0 0 10 10"><path d="M0 1.5h10v7H0zm1 1v.3l4 2.7 4-2.7v-.3z"/></svg>info@farviewcapital.com</li>
        <li><svg viewBox="0 0 10 10"><circle cx="5" cy="5" r="5"/></svg>www.farviewcapital.com</li>
      </ul>
    </div>
  </section>
</body>
</html>
```